Velomark advertisement one page flyer design

We need a flyer design for our company to advertise what we offer, it only needs to be one sided, approx A5 in size.
Our logo: http://velomark.example/images/logo.png (I will provide in high-res later)
We offer, website design, development, bespoke applications. We would like to advertise that we can be hired for short term contracts for companies who need help with their work load.
Some of, but not limited to the systems we build are content management systems, e-commerce systems & event booking systems.
Our strap line is "We design, develop and deliver", a nice sleek redesign of the image on our website would be nice, but not required 100% - http://velomark.example/
Other details to put on the flyer:-
Email: hello@velomark.example
Tel: 01632 960 417
Address: Velomark Ltd, Bright Suites, Fenwick Row, Harrowby, ZX12 4QT
We welcome any other ideas.

```html
<!DOCTYPE html>
<html lang="en">
<head>
<meta charset="utf-8">
<title>Velomark flyer</title>
<link href="https://fonts.googleapis.com/css2?family=Orbitron:wght@600;700&family=PT+Sans:wght@400;700&display=swap" rel="stylesheet">
<style>
:root{
  --orange:#f07d1a;
  --backdrop:#e4e4e4;
  --paper:#ffffff;
  --mist:#e3e3e3;
  --slate:#8c8c8c;
  --slate-light:#9d9d9d;
  --charcoal:#454545;
  --strip:#5b5b5b;
  --ink:#2f2f2f;
  --icon:#c9c9c9;
}
*{box-sizing:border-box;margin:0;padding:0}
html,body{width:1200px;height:850px;overflow:hidden;background:var(--backdrop)}
body{position:relative;font-family:"PT Sans",sans-serif;color:var(--ink)}
.flyer{position:absolute;left:314px;top:39px;width:540px;height:760px;background:var(--paper);overflow:hidden}
.block{position:absolute}
.topbar-square{position:absolute;top:37px;width:16px;height:10px;background:var(--orange)}
.brand{position:absolute;right:16px;top:18px;display:flex;align-items:center;gap:6px;font-family:"PT Sans",sans-serif;font-weight:700;font-size:30px;color:var(--charcoal);letter-spacing:.5px}
.brand-dot{width:16px;height:16px;border-radius:50%;background:var(--orange)}
.intro{left:0;top:56px;width:540px;height:254px;background:var(--mist)}
.strapline{position:absolute;left:49px;top:17px;font-family:"Orbitron",sans-serif;font-weight:700;font-size:21px;color:var(--orange);letter-spacing:.2px;white-space:nowrap}
.intro-copy{position:absolute;left:50px;top:51px;width:478px;font-size:14.6px;line-height:18.3px;color:var(--ink)}
.process{position:absolute;left:0;top:150px}
.cms-left{left:0;top:309px;width:209px;height:82px;background:linear-gradient(90deg,#8a8a8a,#a3a3a3)}
.strip{background:var(--strip)}
.feature-band{background:var(--slate);color:#fff;padding:3px 10px 0 10px}
.feature-title{font-family:"Orbitron",sans-serif;font-weight:600;font-size:14px;color:var(--orange);letter-spacing:.6px;line-height:18px}
.feature-copy{font-size:14.3px;line-height:18.3px;color:#fff}
.contact{left:0;top:391px;width:210px;height:160px;background:var(--charcoal);color:#fff;font-size:14.3px;line-height:18.6px;font-style:normal}
.contact-lines{position:absolute;right:8px;top:10px;text-align:right}
.contact-icons{position:absolute;left:24px;top:13px}
.features{left:230px;font-size:14.3px;line-height:18.5px}
.features h3{font-size:15.2px;font-weight:700;margin:0 0 4px 20px;color:var(--ink)}
.features ul{list-style:none}
.features li{position:relative;padding-left:18px}
.features li::before{content:"";position:absolute;left:0;top:7px;width:10px;height:7px;background:var(--orange)}
.accent-square{top:512px;width:37px;height:26px;background:var(--orange)}
.lower-left-light{left:0;top:551px;width:210px;height:90px;background:var(--slate-light)}
.lower-left-dark{left:0;top:641px;width:210px;height:119px;background:var(--charcoal)}
</style>
</head>
<body>
<main class="flyer">
  <div class="topbar-square" style="left:2px"></div>
  <div class="topbar-square" style="left:58px"></div>
  <div class="topbar-square" style="left:114px"></div>
  <div class="topbar-square" style="left:170px"></div>
  <div class="topbar-square" style="left:226px"></div>
  <div class="topbar-square" style="left:282px"></div>
  <div class="topbar-square" style="left:337px"></div>
  <div class="brand"><span class="brand-dot"></span>Velomark</div>

  <section class="block intro">
    <h1 class="strapline">WE DESIGN, DEVELOP AND DELIVER</h1>
    <p class="intro-copy">We pride ourselves on providing second to none, personal and friendly customer service, our clients are like part of the family. We workclosely together to design, build and deliver a solution that not only matches their vision but also goes that extra mile to ensure it is as user, search engine and mobile friendly.</p>
    <svg class="process" width="540" height="104" viewBox="0 0 540 104">
      <g fill="none" stroke="var(--icon)" stroke-width="5">
        <circle cx="111" cy="53" r="47"/>
        <circle cx="269" cy="53" r="47"/>
        <circle cx="426" cy="53" r="47"/>
      </g>
      <g fill="var(--icon)">
        <rect x="160" y="51" width="20" height="5"/><path d="M178 45 L190 53.5 L178 62 Z"/>
        <rect x="318" y="51" width="20" height="5"/><path d="M336 45 L348 53.5 L336 62 Z"/>
      </g>
      <g fill="#f4f4f4">
        <rect x="81" y="23" width="60" height="60" rx="8" role="img" aria-label="Design icon: pencil and brush"/>
        <rect x="239" y="23" width="60" height="60" rx="8" role="img" aria-label="Develop icon: wrench and screwdriver"/>
        <rect x="396" y="23" width="60" height="60" rx="8" role="img" aria-label="Deliver icon: hand truck with boxes"/>
      </g>
    </svg>
  </section>

  <div class="block cms-left"></div>
  <div class="block strip" style="left:209px;top:309px;width:32px;height:82px"></div>
  <section class="block feature-band" style="left:241px;top:309px;width:299px;height:82px">
    <h2 class="feature-title">CONTENT MANAGEMENT</h2>
    <p class="feature-copy">Our content management system has been developed from the ground-up with ease of use as the main emphasis.</p>
  </section>

  <address class="block contact">
    <svg class="contact-icons" width="16" height="56" viewBox="0 0 16 56" fill="none" stroke="#fff" stroke-width="1.6">
      <circle cx="7" cy="6" r="2.4"/><path d="M9.4 4v3.2c0 1.6 2.6 1.6 2.6-1.2A5 5 0 1 0 9 10.6"/>
      <path d="M3 21c0 5 4 9 9 9l1.4-2-2.6-1.6-1.3 1.2c-1.8-.8-3.3-2.3-4.1-4.1l1.2-1.3L5 18.6 3 20z" fill="#fff" stroke="none"/>
      <rect x="1" y="40" width="13" height="9" fill="#fff" stroke="none"/><path d="M1 40l6.5 5 6.5-5" stroke="#888" stroke-width="1"/>
    </svg>
    <div class="contact-lines">
      hello@velomark.example<br>
      01632 960 417<br>
      Velomark Ltd,<br>
      Bright Suites, Fenwick Row,<br>
      Harrowby, ZX12 4QT
    </div>
  </address>

  <section class="block features" style="top:401px">
    <h3>A few of the other features include:</h3>
    <ul>
      <li>Easy to use WYSIWYG</li>
      <li>Version Control</li>
      <li>Media Centre</li>
      <li>Mutli-tier access levels</li>
    </ul>
  </section>

  <div class="block strip" style="left:208px;top:512px;width:33px;height:32px"></div>
  <div class="block accent-square" style="left:266px"></div>
  <div class="block accent-square" style="left:344px"></div>
  <div class="block accent-square" style="left:421px"></div>
  <div class="block accent-square" style="left:498px"></div>

  <div class="block lower-left-light"></div>
  <div class="block lower-left-dark"></div>
  <div class="block" style="left:210px;top:551px;width:31px;height:209px;background:var(--paper)"></div>

  <section class="block feature-band" style="left:241px;top:547px;width:299px;height:99px">
    <h2 class="feature-title">E-COMMERCE SYSTEM</h2>
    <p class="feature-copy">Our e-commerce system is simple yet extremely powerful. If you are selling t-shirts, books or even downloadable content, this is supported out the of the box.</p>
  </section>

  <section class="block features" style="top:655px">
    <h3>A few other features include:</h3>
    <ul>
      <li>Unlimited Products</li>
      <li>Advanced search</li>
      <li>Customer relationship system</li>
      <li>Integrated credit card payments and Payvault</li>
    </ul>
  </section>
</main>
</body>
</html>
```